Quick Order Banner Design

We want to build a banner that will sit in the middle of the page that will replace our current quick order banner that we don't like. See https://www.snapvellum.com/image/48230917?key=3f91ac2de7b4c8e05a6d1f29b73e4c0a

Text:
Quick Order is a fast and easy way to fill your cart with items when you know exactly what you want to purchase.

Design ideas:

Use foto Noto Sans. Color codes can be of #00539E, FDBC38, #6AC07A

We don't want a computer screen in banner nor a person. You can look at our competitors below for ideas.

i don't like the design here https://tovirapartsdepot.com/blog/post/order-parts-fast-with-our-new-quick-order-feature but the concept is cool as it shows where to access it.. but i want other ideas too.

Our staging server is plimdex4.com

Our competitors:
https://www.halvorsupplyco.com/
https://www.lumbrix.com/
https://www.vosko.com/
https://www.quelt.com/index.html

Target Market(s)

B2B, Contractors who buy our products

Industry/Entity Type

hvac

Requirements
Should not have
• people photos or computer or computer screens.

```html
<!DOCTYPE html>
<html lang="en">
<head>
<meta charset="utf-8">
<title>Quick Order Banner</title>
<link rel="stylesheet" href="https://fonts.googleapis.com/css2?family=Noto+Sans:wght@400;600;700;800&display=swap">
<style>
:root{
  --stage:#6b6b6b;
  --blue-deep:#173a8c;
  --blue:#00539E;
  --blue-light:#2f7fd0;
  --yellow:#FDBC38;
  --green:#6AC07A;
  --white:#ffffff;
  --ink:#3d3d3d;
  --muted:#777777;
  --line:#d9d9d9;
  --side:#8a8b8d;
  --side-dark:#6f7072;
  --btn:#0b4f9c;
  --orange:#f47a20;
  --qty:#55595e;
}
*{box-sizing:border-box;margin:0;padding:0}
html,body{width:1200px;height:508px;overflow:hidden;background:var(--stage);font-family:"Noto Sans",Arial,sans-serif}
.canvas{position:relative;width:1200px;height:508px}
.banner{position:absolute;left:38px;top:88px;width:1127px;height:322px;overflow:hidden}
.banner-bg{position:absolute;inset:0}
.headline{position:absolute;left:40px;top:42px;color:var(--yellow);font-weight:700;font-size:74px;line-height:1;letter-spacing:.5px}
.tagline{position:absolute;left:40px;top:134px;width:580px;color:var(--white);font-weight:700;font-size:27px;line-height:40px}
.order-card-shadow{position:absolute;left:628px;top:16px;width:484px;height:293px;background:#e6e6e6}
.order-card{position:absolute;left:637px;top:9px;width:483px;height:291px;background:var(--white);color:var(--ink)}
.card-title{position:absolute;left:11px;top:4px;font-size:14px;font-weight:700;color:#444}
.card-intro{position:absolute;left:11px;top:27px;width:440px;font-size:5px;line-height:7px;color:var(--muted)}
.table-head{position:absolute;left:10px;top:55px;width:333px;height:24px;border-top:1px solid var(--line);border-bottom:1px solid var(--line);font-size:5.5px;font-weight:700;color:#555}
.table-head span{position:absolute;top:8px}
.row{position:absolute;left:10px;width:333px;height:26px;border-bottom:1px solid var(--line)}
.row input,.field{position:absolute;left:5px;top:4px;width:165px;height:17px;border:1px solid #c8c8c8;font-size:5px;color:#555;padding-left:6px;line-height:15px;background:var(--white)}
.field.empty{color:#888}
.thumb{position:absolute;left:184px;top:2px;width:18px;height:21px;background:linear-gradient(#8a6a4a,#5b4330)}
.qty-btn{position:absolute;top:5px;width:16px;height:16px;background:var(--qty);color:var(--white);font-size:10px;font-weight:700;text-align:center;line-height:15px}
.qty-btn.minus{left:215px}.qty-btn.plus{left:252px}
.qty-val{position:absolute;left:231px;top:5px;width:21px;height:16px;border-top:1px solid #ccc;border-bottom:1px solid #ccc;font-size:5.5px;text-align:center;line-height:14px}
.price{position:absolute;left:281px;top:10px;font-size:5px;color:#555}
.trash{position:absolute;left:320px;top:9px;width:5px;height:7px;background:#666;border-radius:0 0 1px 1px}
.trash::before{content:"";position:absolute;left:-1px;top:-2px;width:7px;height:1px;background:#666}
.add-rows{position:absolute;left:15px;top:232px;font-size:5px;color:var(--blue)}
.subtotal{position:absolute;left:255px;top:246px;font-size:5.5px;font-weight:700;color:#444}
.btn{position:absolute;background:var(--btn);color:var(--white);font-size:5px;font-weight:600;text-align:center}
.btn.cart{left:260px;top:258px;width:57px;height:15px;line-height:15px}
.sidebar{position:absolute;left:343px;top:55px;width:107px;height:227px;background:var(--side);color:var(--white)}
.side-import{position:absolute;left:0;top:0;width:107px;height:114px}
.side-paste{position:absolute;left:0;top:114px;width:107px;height:113px;background:var(--side-dark)}
.side-title{position:absolute;left:8px;font-size:5.5px;font-weight:700;display:flex;align-items:center;gap:4px}
.side-title i{display:inline-block;width:6px;height:7px;background:var(--white)}
.drop-zone{position:absolute;left:6px;top:24px;width:95px;height:65px;border:1px dashed #c9c9c9;font-size:4.5px;line-height:6px;text-align:center;padding:7px 6px 0}
.btn.choose{left:17px;top:32px;width:57px;height:11px;line-height:11px}
.csv-link{position:absolute;left:0;right:0;top:50px;font-size:4.5px;text-decoration:underline}
.btn.tutorial{left:24px;top:96px;width:57px;height:11px;line-height:11px;background:var(--orange)}
.paste-copy{position:absolute;left:7px;top:20px;width:95px;font-size:4.5px;line-height:6px}
.paste-box{position:absolute;left:6px;top:48px;width:94px;height:42px;background:var(--white);color:#555;font-size:4.5px;line-height:6px;padding:4px 5px}
.btn.paste-cart{left:6px;top:95px;width:94px;height:12px;line-height:12px}
</style>
</head>
<body>
<div class="canvas">
  <section class="banner">
    <svg class="banner-bg" width="1127" height="322" viewBox="0 0 1127 322" aria-hidden="true">
      <defs>
        <linearGradient id="blueField" x1="0" y1="0" x2="1" y2="0">
          <stop offset="0" stop-color="#183c8d"/>
          <stop offset="0.6" stop-color="#0a4f9f"/>
          <stop offset="1" stop-color="#0b63b4"/>
        </linearGradient>
      </defs>
      <rect width="1127" height="322" fill="url(#blueField)"/>
      <polygon points="330,322 420,322 690,0 600,0" fill="#2f7fd0" opacity=".18"/>
      <polygon points="420,322 470,322 740,0 690,0" fill="#5aa0e0" opacity=".15"/>
      <polygon points="180,322 230,322 500,0 450,0" fill="#2f7fd0" opacity=".1"/>
      <polygon points="477,322 560,322 800,40 720,40" fill="var(--green)"/>
      <polygon points="552,322 1127,322 1127,0 752,0" fill="var(--yellow)"/>
    </svg>

    <h1 class="headline">Quick Order</h1>
    <p class="tagline">is a fast and easy way to fill your cart with items when you know exactly what you want to purchase.</p>

    <div class="order-card-shadow"></div>
    <div class="order-card">
      <h2 class="card-title">Quick Order</h2>
      <p class="card-intro">Quick Order is the fastest and easiest way to place your orders online. You can use the single item search below to enter product name / SKU or use the bulk csv import option.</p>

      <div class="table-head">
        <span style="left:6px">Product Name / SKU</span>
        <span style="left:182px">Photo</span>
        <span style="left:236px">Qty</span>
        <span style="left:281px">Price</span>
      </div>

      <div class="row" style="top:79px;height:34px">
        <div class="field" style="top:8px">Corvane, KRT48C20M</div>
        <div class="thumb" role="img" aria-label="Product photo of a condensing unit" style="top:6px"></div>
        <div class="qty-btn minus" style="top:9px">−</div><div class="qty-val" style="top:9px">1</div><div class="qty-btn plus" style="top:9px">+</div>
        <div class="price" style="top:14px">$3,410.00</div><div class="trash" style="top:13px"></div>
      </div>
      <div class="row" style="top:113px;height:34px">
        <div class="field" style="top:8px">Corvane, HLX24D31</div>
        <div class="thumb" role="img" aria-label="Product photo of an air handler" style="top:6px;left:188px;width:12px"></div>
        <div class="qty-btn minus" style="top:9px">−</div><div class="qty-val" style="top:9px">1</div><div class="qty-btn plus" style="top:9px">+</div>
        <div class="price" style="top:14px">$1,070.00</div><div class="trash" style="top:13px"></div>
      </div>
      <div class="row" style="top:147px">
        <div class="field empty">Enter Product Name or SKU to Add</div>
        <div class="qty-btn minus">−</div><div class="qty-val"></div><div class="qty-btn plus">+</div>
        <div class="price">$0.00</div><div class="trash"></div>
      </div>
      <div class="row" style="top:173px">
        <div class="field empty">Enter Product Name or SKU to Add</div>
        <div class="qty-btn minus">−</div><div class="qty-val"></div><div class="qty-btn plus">+</div>
        <div class="price">$0.00</div><div class="trash"></div>
      </div>
      <div class="row" style="top:199px">
        <div class="field empty">Enter Product Name or SKU to Add</div>
        <div class="qty-btn minus">−</div><div class="qty-val"></div><div class="qty-btn plus">+</div>
        <div class="price">$0.00</div><div class="trash"></div>
      </div>

      <div class="add-rows">+ Add Additional Rows</div>
      <div class="subtotal">Subtotal: $4,480.00</div>
      <div class="btn cart">Add To Cart</div>

      <aside class="sidebar">
        <div class="side-import">
          <div class="side-title" style="top:8px"><i></i>Import Your Order</div>
          <div class="drop-zone">Drag and drop a .csv file here, or select file from your computer to import to cart.
            <div class="btn choose">Choose File</div>
            <div class="csv-link">Download Sample CSV</div>
          </div>
          <div class="btn tutorial">ⓘ Tutorial</div>
        </div>
        <div class="side-paste">
          <div class="side-title" style="top:7px"><i></i>Paste Your Order</div>
          <p class="paste-copy">Copy and paste or manually enter your order with the SKU # and quantity, separated by a comma on each line.</p>
          <div class="paste-box">Example:<br><br>KRT48C20M,1<br>HLX24D31-0600,2</div>
          <div class="btn paste-cart">Add to Cart</div>
        </div>
      </aside>
    </div>
  </section>
</div>
</body>
</html>
```